We are looking for a new website design for our SEO WEB Development Company. The URL is www.brellowcreativeworks.com

We want it to be a more powerful representation of what we do. We are also looking for a number of designers that we will give continuous business to every month. The persons design we choose will also get a proposal to complete 4 - 6 new designs for us every month for our clients.

Be creative as you can in your design submissions. We really want to stand out!

Just to give you an idea of what we like look at this site: http://www.tovandigitalstudio.com/

```html
<!DOCTYPE html>
<html lang="en">
<head>
<meta charset="utf-8">
<title>Brellow Interactive Group</title>
<link rel="stylesheet" href="https://fonts.googleapis.com/css2?family=Arimo:wght@400;700&family=Cinzel:wght@700&family=Tinos:wght@400;700&display=swap">
<style>
:root{
  --black:#050505;
  --panel:#1b1b1b;
  --cyan:#3ec6f0;
  --blue-deep:#0b2a44;
  --blue-mid:#1b6f9c;
  --ink:#2b2b2b;
  --white:#ffffff;
  --grey:#9a9a9a;
  --red:#e0261e;
  --green:#52b634;
}
*{margin:0;padding:0;box-sizing:border-box}
html,body{width:911px;height:1200px;overflow:hidden;background:var(--black)}
body{position:relative;font-family:Arimo,Arial,sans-serif;color:var(--white)}
.abs{position:absolute}
.topbar{left:0;top:0;width:911px;height:45px;background:linear-gradient(#1a1a1a,#000)}
.search{left:736px;top:8px;width:137px;height:21px;background:#f2f2f2;border-radius:3px;font-style:italic;color:#bbb;font-size:13px;padding:3px 22px}
.search-btn{left:879px;top:6px;width:25px;height:25px;background:var(--green);border-radius:4px}
.header{left:0;top:45px;width:911px;height:84px;background:var(--white)}
.brand{left:20px;top:66px;display:flex;align-items:center;gap:10px;font-family:Arimo,Arial,sans-serif;font-weight:700;font-size:22px;color:var(--ink)}
.brand .mark{width:26px;height:26px;background:var(--ink)}
.nav{left:328px;top:101px;width:583px;height:30px;background:#0d0d0d;display:flex;align-items:center;font-size:12px}
.nav a{color:var(--cyan);text-decoration:none;padding:0 7px;border-right:1px solid #555;margin-left:2px}
.nav .contact{margin-left:auto;display:flex;align-items:center;gap:6px;color:var(--white);font-weight:700;font-size:11px;padding-right:8px}
.ico-phone{width:26px;height:26px;background:var(--green);border-radius:3px;display:flex;align-items:center;justify-content:center}
.hero{left:0;top:129px;width:911px;height:188px;background:radial-gradient(ellipse at 55% 40%,#3aa0d2 0%,var(--blue-mid) 30%,var(--blue-deep) 70%,#05101b 100%)}
.hero-title{left:20px;top:196px;font-family:Cinzel,serif;font-size:38px;text-shadow:2px 2px 4px #000}
.hero-tag{left:624px;top:154px;font-weight:700;font-size:15px;line-height:18px}
.intro{left:0;top:317px;width:320px;height:340px;background:var(--black);padding:4px 20px;font-size:7.6px;line-height:9.2px;color:#ddd}
.intro p{margin-bottom:8px}
.intro b{font-family:Tinos,serif;color:#8fd0ff;font-size:9px}
.quote{left:321px;top:317px;width:418px;height:256px;background:#222;border-top:1px solid #444;padding:30px 3px 0 4px}
.quote h2{font-family:Tinos,serif;font-size:17px;margin:0 0 14px;color:#f0f0f0}
.quote p{font-size:11.4px;line-height:13.4px;color:#eee}
.form{left:740px;top:317px;width:171px;height:256px;background:#111;padding:36px 6px 0 6px}
.form label{display:block;font-size:12px;line-height:12px;font-weight:700;margin-bottom:3px}
.form .field{height:19px;background:var(--white);border:1px solid #888;margin-bottom:14px}
.form .btn{margin-top:2px;height:22px;background:linear-gradient(#5a8fd8,#2d5aa8);border-radius:3px;font-size:10px;font-weight:700;text-align:center;line-height:22px}
.blog{left:321px;top:573px;width:590px;height:84px;background:#0a0a0a;padding:2px 6px}
.blog h3{font-size:15px;font-weight:700;margin-bottom:4px}
.blog h3 span{color:var(--red)}
.blog-grid{display:grid;grid-template-columns:repeat(5,1fr);row-gap:5px;font-size:6px;color:#aaa;padding-left:6px}
.blog-grid div::before{content:"› ";color:#ddd}
.lower{left:0;top:657px;width:413px;height:343px;background:linear-gradient(#1a1a1a,#2a2a2a)}
.cam{left:54px;top:673px;width:72px;height:72px;background:linear-gradient(#5a8ec4,#1d3557);border:3px solid #ddd}
.news{left:140px;top:673px;width:257px;height:107px;background:linear-gradient(#1c4c6c,#0e2a3e);border-radius:6px;padding:14px 16px;font-size:8.5px}
.news li{list-style:none;color:var(--cyan);text-decoration:underline;margin-bottom:4px}
.news li::before{content:"■ ";font-size:6px;text-decoration:none}
.news .more{display:inline-block;margin-top:6px;background:#2c3c4a;color:#9ab;padding:1px 8px;font-size:8px;text-decoration:none}
.social{left:23px;top:787px;width:377px;height:210px;background:#6c5a47;display:flex;gap:6px;padding:4px}
.social .follow{position:absolute;left:6px;top:10px;font-size:10px;font-weight:700;color:#eee;z-index:2}
.tile{flex:1;background:linear-gradient(#8f7a60,#5a4a38);position:relative}
.tile .sq{position:absolute;left:10px;top:46px;width:30px;height:30px;border-radius:4px}
.tile .lbl{position:absolute;left:50%;top:140px;transform:translate(-50%,-50%) rotate(-90deg);font-size:9px;color:#eee;white-space:nowrap}
.promo{left:413px;top:667px;width:483px;height:330px;background:var(--white)}
.promo-photo{left:413px;top:737px;width:483px;height:260px;background:linear-gradient(135deg,#f3f3f3,#cfd4d8 40%,#3a3a3a 75%,#e8e8e8)}
.promo-t1{left:442px;top:683px;font-size:20px;color:#111;letter-spacing:.5px}
.promo-t1 span,.promo-t2 span{color:#2a8fd6}
.promo-t2{left:559px;top:707px;font-size:20px;color:#111}
.share{left:0;top:1000px;width:911px;height:40px;background:#000;font-size:8.5px;font-weight:700}
.share .fb{position:absolute;left:90px;top:8px;display:flex;align-items:center;gap:5px}
.share .fb i{width:11px;height:11px;background:#3b5998;display:block}
.call{position:absolute;left:676px;top:4px;display:flex;align-items:center;gap:8px;font-size:10px}
.call .dot{width:40px;height:40px;border-radius:50%;background:#eee;display:flex;align-items:center;justify-content:center}
.call .lbl{color:var(--green);font-weight:400}
.footer{left:0;top:1040px;width:911px;height:160px;background:linear-gradient(#0c0c0c,#000)}
.fcol{top:1048px;font-size:8.5px;color:var(--grey);line-height:10.5px}
.fcol h4{color:var(--cyan);font-size:9.5px;margin-bottom:13px;font-weight:700}
.frule{left:22px;top:1066px;width:866px;height:1px;background:#333}
.engines{left:684px;top:1102px;display:flex;gap:3px}
.engines i{display:block;width:40px;height:17px;background:#e4e4e4;border-radius:2px}
.copy{left:713px;top:1178px;font-size:7px;color:#aaa}
</style>
</head>
<body>
<div class="abs topbar"></div>
<div class="abs search">Search</div>
<div class="abs search-btn"></div>

<div class="abs header"></div>
<div class="abs brand"><i class="mark"></i><span>Brellow Interactive Group</span></div>
<nav class="abs nav">
  <a>Creative Design</a><a>Website Design</a><a>Internet Marketing</a><a style="border:0">IT Consulting</a>
  <div class="contact"><span class="ico-phone"><svg width="16" height="16" viewBox="0 0 24 24"><path fill="#fff" d="M6.6 10.8a15 15 0 006.6 6.6l2.2-2.2a1 1 0 011-.25 11.4 11.4 0 003.6.6 1 1 0 011 1V20a1 1 0 01-1 1A17 17 0 013 4a1 1 0 011-1h3.5a1 1 0 011 1c0 1.25.2 2.45.6 3.6a1 1 0 01-.25 1z"/></svg></span>Contact us 877-555-0148</div>
</nav>

<div class="abs hero" role="img" aria-label="Blue abstract light background"></div>
<div class="abs hero-tag">Focusing on your brand<br>With the right Internet Marketing tools</div>
<h1 class="abs hero-title">Media Marketing Experts</h1>

<section class="abs intro">
  <p><b>Brellow Interactive Group</b> is a leading Dallas Web Site Design, Publishing and Internet Marketing Firm. Our Dallas Texas based Website Design and Internet Marketing experts are some of the best in the industry!</p>
  <p><b>Brellow Interactive Web</b> is a full-service Dallas based Advertising Agency comprised of experienced advertising and marketing professionals that provide clients with a clear and distinct voice in the marketplace. Web Site Design and Internet Marketing experts at our Dallas location specialize in developing Online Marketing Strategies, Search Engine Marketing and Optimization (SEO), Pay Per Click, Web Site Design and Development, and Online Reputation Management.</p>
  <p><b>Brellow Interactive Publishing</b> provides full-service custom publishing and consulting services for magazines, newsletters, blogs and web sites. We are the complete interactive publishing arm for your organization. Our services include: Strategic Planning and Computer Modeling; Art Direction and Design; Production Services; Circulation Marketing and Management; Subscription Fulfillment Management; Advertising Sales Management; Web Site and Digital Magazine Design and Management; and Video Streaming Services.</p>
  <p><b>Brellow Interactive Media</b> provides cost-effective Web Site Design services, Search Engine Marketing, Internet Advertising, Internet Marketing Campaigns and most important, we can accommodate any budget.</p>
  <p><b>Brellow Interactive Reputation Management and Repair</b> provides reputation management and repair services to the online community. We offer a plan of action to create a process of tracking an entity's actions and other entities' opinions about those actions; reporting on those actions and opinions; and reacting to that report creating a feedback loop. Reputation management has become essential with the advent of widespread computing. Reputation management systems use predefined criteria for processing complex data to report the many factors affecting a company's reputation. However, these systems only facilitate and automate the process of determining trustworthiness.</p>
</section>

<section class="abs quote">
  <h2>Get A Free Reputation Management &amp; Repair Quote!</h2>
  <p>The goal of a reputation management or repair campaign is to create and/or strengthen an authoritative, positive image of your company by helping you gain positive name recognition across a wide range of websites. Most Search Engine users only pay attention to the Top 20 results, which is what we focus on. We will work closely with you to come up with a strong, detailed plan to put you at the top of search engins such as Searchly.com and above the negative listings about you. We will analyze your situation closely and create a detailed but flexible plan for your Reputation Management Campaign.</p>
</section>

<form class="abs form">
  <label>Name</label><div class="field"></div>
  <label>Phone Number</label><div class="field"></div>
  <label>Email</label><div class="field"></div>
  <label>Website &nbsp;Address</label><div class="field"></div>
  <div class="btn">Request For &nbsp;Quote</div>
</form>

<section class="abs blog">
  <h3>Latests from <span>Blog</span></h3>
  <div class="blog-grid">
    <div>FLEETS</div><div>MEDIUM TRUCK</div><div>MEDIUM TRUCK</div><div>MEDIUM TRUCK</div><div>MEDIUM TRUCK</div>
    <div>COMMERCIAL</div><div>SPECIALTY TIRES</div><div>SPECIALTY TIRES</div><div>SPECIALTY TIRES</div><div>SPECIALTY TIRES</div>
    <div>WHOLESALE</div><div>LOADERS</div><div>LOADERS</div><div>LOADERS</div><div>LOADERS</div>
    <div>INDIVIDUAL AND AUTOMOTIVE</div><div>INDIVIDUAL AND AUTOMOTIVE</div><div>INDIVIDUAL AND AUTOMOTIVE</div><div>INDIVIDUAL AND AUTOMOTIVE</div><div>INDIVIDUAL AND AUTOMOTIVE</div>
  </div>
</section>

<div class="abs lower"></div>
<div class="abs cam" role="img" aria-label="Camera in front of a framed photo"></div>
<ul class="abs news">
  <li>Lorem ipsum dolor sit amet, consectetuer adipiscing elit.</li>
  <li>Proin pellentesque nulla sit amet nisi.</li>
  <li>Phasellus tincidunt pede et dolor.</li>
  <li>Cras ut massa varius eros tempor fringilla.</li>
  <li>Mauris varius vulputate nulla.</li>
  <span class="more">» more</span>
</ul>
<div class="abs social">
  <span class="follow">Follow us on</span>
  <div class="tile"><i class="sq" style="background:#7a3c8c"></i><span class="lbl">Bookmarkr</span></div>
  <div class="tile"><i class="sq" style="background:#2fa4b8"></i><span class="lbl">Chirper</span></div>
  <div class="tile"><i class="sq" style="background:#d0462c"></i><span class="lbl">Foxbrowse</span></div>
  <div class="tile"><i class="sq" style="background:#2c6a86"></i><span class="lbl">Friendnet</span></div>
  <div class="tile"><i class="sq" style="background:#7fa43a"></i><span class="lbl">Wanderpage</span></div>
  <div class="tile"><i class="sq" style="background:#d6a21e"></i><span class="lbl">Diggly</span></div>
  <div class="tile"><i class="sq" style="background:#c23a2a"></i><span class="lbl">Feedcast</span></div>
</div>

<div class="abs promo"></div>
<div class="abs promo-photo" role="img" aria-label="Business team working together around a laptop in a bright office"></div>
<div class="abs promo-t1">NOT ONLY <span>BRELLOW.</span></div>
<div class="abs promo-t2">BUT <span>SOLUTIONS.</span></div>

<div class="abs share">
  <div class="fb"><i></i>Share on Friendnet</div>
  <div class="call"><span class="dot"><svg width="20" height="20" viewBox="0 0 24 24"><path fill="#111" d="M6.6 10.8a15 15 0 006.6 6.6l2.2-2.2a1 1 0 011-.25 11.4 11.4 0 003.6.6 1 1 0 011 1V20a1 1 0 01-1 1A17 17 0 013 4a1 1 0 011-1h3.5a1 1 0 011 1c0 1.25.2 2.45.6 3.6a1 1 0 01-.25 1z"/></svg></span><span><span class="lbl">Call us for a quote today:</span> 214-555-0193</span></div>
</div>

<footer class="abs footer"></footer>
<div class="abs frule"></div>
<div class="abs fcol" style="left:32px"><h4>Creative Design</h4>Creative Advertising<br>Print Design<br>Corporate Identity<br>Packaging</div>
<div class="abs fcol" style="left:176px"><h4>Internet Marketing Services</h4>Search Engine Optimization<br>Pay-per-Click Campaign Consulting<br>Email Marketing<br>SEO Copywriting<br>Reputation Management</div>
<div class="abs fcol" style="left:361px"><h4>Website Design</h4>Web Design<br>E-commerce<br>Multimedia<br>Web Application Development</div>
<div class="abs fcol" style="left:501px"><h4>IT Consulting Brellow Interactive</h4>About Us<br>Our Work<br>Contact Us</div>
<div class="abs engines"><i></i><i></i><i></i><i></i><i></i></div>
<div class="abs copy">Copyright 2011 Brellow Interactive Group reserved all rights</div>
</body>
</html>
```